Data Collection Workbook

We are creating a data gathering booklet that will be completed by our clients (ages 40-90). Due to the volume of information being collected, we are looking for a format that is both inviting to complete and aesthetically pleasing to the eye. The final product will be approximately 20-30 pages, divided into 13 sections. A table of contents, as well as two sample pages are attached.

```html
<!DOCTYPE html>
<html lang="en">
<head>
<meta charset="utf-8">
<title>General Information</title>
<link rel="stylesheet" href="https://fonts.googleapis.com/css2?family=Questrial&family=Open+Sans:wght@600&display=swap">
<style>
  :root {
    --paper: #ffffff;
    --ink: #3a3a3a;
    --rule: #6f6f6f;
    --frame: #8a8a8a;
    --accent: #3fb2c4;
  }
  html, body {
    margin: 0;
    padding: 0;
    width: 848px;
    height: 1200px;
    overflow: hidden;
    background: var(--paper);
  }
  .page {
    position: relative;
    width: 848px;
    height: 1200px;
    background: var(--paper);
    font-family: "Open Sans", Arial, sans-serif;
    color: var(--ink);
  }
  .edge-line {
    position: absolute;
    top: 0;
    width: 1px;
    height: 1200px;
    background: var(--frame);
  }
  .edge-line--outer { left: 3px; }
  .edge-line--margin { left: 47px; }
  .section-title {
    position: absolute;
    left: 31px;
    top: 120px;
    margin: 0;
    display: flex;
    align-items: center;
    font-family: "Questrial", "Century Gothic", sans-serif;
    font-weight: 400;
    font-size: 31px;
    letter-spacing: 0.2px;
    color: var(--accent);
  }
  .section-title::before {
    content: "";
    width: 32px;
    height: 1.5px;
    margin-right: 5px;
    background: var(--frame);
  }
  .form {
    position: absolute;
    left: 64px;
    top: 180px;
    width: 720px;
  }
  .form-row {
    display: grid;
    height: 49.4px;
    align-items: center;
  }
  .form-row--single { grid-template-columns: 1fr; }
  .form-row--wide { grid-template-columns: 512px 1fr; }
  .form-row--phone { grid-template-columns: 409px 1fr; }
  .form-row--contact { grid-template-columns: 358px 205px 1fr; }
  .form-row--deposit { grid-template-columns: 358px 1fr; }
  .field {
    display: flex;
    align-items: baseline;
    font-size: 11.5px;
    font-weight: 600;
    white-space: nowrap;
  }
  .field-label { flex: none; }
  .field-line {
    flex: 1;
    height: 0;
    margin: 0 5px 0 4px;
    border-bottom: 1px solid var(--rule);
  }
  .field--gap .field-line { margin-left: 14px; }
  .field:last-child .field-line { margin-right: 0; }
</style>
</head>
<body>
<div class="page">
  <div class="edge-line edge-line--outer"></div>
  <div class="edge-line edge-line--margin"></div>

  <h1 class="section-title">GENERAL INFORMATION</h1>

  <div class="form">
    <div class="form-row form-row--single">
      <div class="field field--gap"><span class="field-label">My full legal name</span><span class="field-line"></span></div>
    </div>
    <div class="form-row form-row--single">
      <div class="field field--gap"><span class="field-label">My date of birth Locaion(City/State)</span><span class="field-line"></span></div>
    </div>
    <div class="form-row form-row--single">
      <div class="field field--gap"><span class="field-label">My social security number</span><span class="field-line"></span></div>
    </div>
    <div class="form-row form-row--wide">
      <div class="field"><span class="field-label">My driver's license number (or DMV identification number)</span><span class="field-line"></span></div>
      <div class="field"><span class="field-label">State</span><span class="field-line"></span></div>
    </div>
    <div class="form-row form-row--wide">
      <div class="field"><span class="field-label">My passprt number</span><span class="field-line"></span></div>
      <div class="field"><span class="field-label">City/State Issued</span><span class="field-line"></span></div>
    </div>
    <div class="form-row form-row--wide">
      <div class="field"><span class="field-label">My address</span><span class="field-line"></span></div>
      <div class="field"><span class="field-label">Ctt State Zip</span><span class="field-line"></span></div>
    </div>
    <div class="form-row form-row--phone">
      <div class="field"><span class="field-label">My telephone numbers: Cell phone</span><span class="field-line"></span></div>
      <div class="field"><span class="field-label">Voicemail Password</span><span class="field-line"></span></div>
    </div>
    <div class="form-row form-row--phone">
      <div class="field field--gap"><span class="field-label">Home phone</span><span class="field-line"></span></div>
      <div class="field"><span class="field-label">Voicemail Password</span><span class="field-line"></span></div>
    </div>
    <div class="form-row form-row--phone">
      <div class="field field--gap"><span class="field-label">Work phone</span><span class="field-line"></span></div>
      <div class="field"><span class="field-label">Voicemail Password</span><span class="field-line"></span></div>
    </div>
    <div class="form-row form-row--phone">
      <div class="field"><span class="field-label">Other phone</span><span class="field-line"></span></div>
      <div class="field"><span class="field-label">Password(s)</span><span class="field-line"></span></div>
    </div>
    <div class="form-row form-row--contact">
      <div class="field"><span class="field-label">My in-state emergency contact</span><span class="field-line"></span></div>
      <div class="field"><span class="field-label">Phone</span><span class="field-line"></span></div>
      <div class="field"><span class="field-label">Relationship</span><span class="field-line"></span></div>
    </div>
    <div class="form-row form-row--contact">
      <div class="field"><span class="field-label">My out- of-state emergency</span><span class="field-line"></span></div>
      <div class="field"><span class="field-label">contact</span><span class="field-line"></span></div>
      <div class="field"><span class="field-label">Relaionship</span><span class="field-line"></span></div>
    </div>
    <div class="form-row form-row--contact">
      <div class="field"><span class="field-label">Child Or close relative/ friend 1</span><span class="field-line"></span></div>
      <div class="field"><span class="field-label">Address</span><span class="field-line"></span></div>
      <div class="field"><span class="field-label">Relationship</span><span class="field-line"></span></div>
    </div>
    <div class="form-row form-row--contact">
      <div class="field"><span class="field-label">Child or close relative/ friend 2</span><span class="field-line"></span></div>
      <div class="field"><span class="field-label">Phone</span><span class="field-line"></span></div>
      <div class="field"><span class="field-label">Relationship</span><span class="field-line"></span></div>
    </div>
    <div class="form-row form-row--contact">
      <div class="field"><span class="field-label">Child or close relative/ friend 3</span><span class="field-line"></span></div>
      <div class="field"><span class="field-label">Address</span><span class="field-line"></span></div>
      <div class="field"><span class="field-label">Relationship</span><span class="field-line"></span></div>
    </div>
    <div class="form-row form-row--contact">
      <div class="field"><span class="field-label">Child or close relative/ friend 4</span><span class="field-line"></span></div>
      <div class="field"><span class="field-label">Phone</span><span class="field-line"></span></div>
      <div class="field"><span class="field-label">Relationship</span><span class="field-line"></span></div>
    </div>
    <div class="form-row form-row--single">
      <div class="field"><span class="field-label">Location &amp; access instructions (combination) for in-home safe or strong box</span><span class="field-line"></span></div>
    </div>
    <div class="form-row form-row--deposit">
      <div class="field"><span class="field-label">Location of Safe depost box(es)</span><span class="field-line"></span></div>
      <div class="field"><span class="field-label">Location of keys</span><span class="field-line"></span></div>
    </div>
    <div class="form-row form-row--single">
      <div class="field"><span class="field-label">List of safe deposi box contents</span><span class="field-line"></span></div>
    </div>
  </div>
</div>
</body>
</html>
```